Lantern Petro - needs a business card

Lantern Petro is a U.S. based diesel sourcing and distribution company that supports American oil & gas fields through providing quality product and consistent services.

Target Market(s)

Oil and Gas

Contact Information for Business Card

The background of the card must be white to ensure the logo pops.

Font styles to use
Serif
Sans Serif

Colors

Designer to choose colors to be used in the design.

Requirements
Must have
• Front of Card: Tag line: Lantern Petro, Powering the Nation's Oil & Gas fields.
• Not sure if you guys do this part but just in case...
• Dale Winterholt
• Owner/CEO
• C:701.555.0148
• E:Dwinterholt@lanternpetro.com
• W:Lanternpetro.com
• Locations: Servicing the Powder River, DJ basin and Bakken formations.
• Back of Card: " Frac fueling is what we do. We understand how important diesel fuel is to your operation, which is why our main service line is Frac fueling. We assure our supply and stand by our service"

```html
<!DOCTYPE html>
<html lang="en">
<head>
<meta charset="utf-8">
<title>Lantern Petro – Business Card</title>
<link href="https://fonts.googleapis.com/css2?family=Open+Sans:ital,wght@0,400;0,600;0,700;0,800;1,700&display=swap" rel="stylesheet">
<style>
  :root{
    --navy:#12306b;
    --navy-deep:#1b2a63;
    --red:#c4161c;
    --red-deep:#a5121a;
    --ink:#3d3d3d;
    --grey:#6b6b6b;
    --rule:#cfcfcf;
    --stage:#2f2f2f;
    --paper:#ffffff;
  }
  *{box-sizing:border-box;margin:0;padding:0}
  html,body{width:1200px;height:866px;overflow:hidden;background:var(--stage)}
  body{font-family:"Open Sans",Arial,sans-serif;display:flex;flex-direction:column;align-items:center;justify-content:center;gap:34px}
  .card{width:640px;height:366px;position:relative;overflow:hidden;box-shadow:0 10px 24px rgba(0,0,0,.45)}

  /* front */
  .card-front{background:var(--paper)}
  .brand{position:absolute;left:300px;top:88px;display:flex;align-items:center;gap:14px}
  .brand-dot{width:46px;height:46px;border-radius:50%;background:var(--navy)}
  .brand-name{font-size:34px;font-weight:800;letter-spacing:1px;color:var(--navy);text-transform:uppercase;line-height:1}
  .tagline{position:absolute;left:300px;top:156px;font-size:9.5px;font-weight:700;color:var(--ink);text-transform:uppercase;letter-spacing:.2px}
  .person{position:absolute;left:40px;top:110px}
  .person-name{font-size:22px;font-weight:600;text-transform:uppercase;line-height:1;letter-spacing:.3px}
  .person-name .first{color:var(--navy)}
  .person-name .last{color:var(--red)}
  .person-role{font-size:14px;color:var(--grey);margin-top:4px}
  .contact{list-style:none;margin-top:12px}
  .contact li{display:flex;align-items:center;gap:8px;font-size:13.5px;color:var(--ink);line-height:1.55}
  .contact svg{width:13px;height:13px;fill:var(--navy);flex:none}
  .divider{position:absolute;left:40px;right:40px;top:262px;height:1px;background:var(--rule)}
  .locations{position:absolute;right:40px;top:276px;width:250px;font-size:15px;color:var(--grey);line-height:1.2}
  .locations .label{color:var(--red)}
  .base-band{position:absolute;left:0;right:0;bottom:0;height:10px;background:linear-gradient(100deg,var(--navy) 0 44%,var(--red) 44% 100%)}

  /* back */
  .card-back{background:linear-gradient(35deg,var(--navy-deep) 0%,#4a1f55 48%,var(--red-deep) 100%);color:#fff;text-align:center;padding:70px 60px 0}
  .back-texture{position:absolute;inset:0;background:radial-gradient(circle at 20% 30%,rgba(255,255,255,.06),transparent 45%),radial-gradient(circle at 85% 70%,rgba(255,255,255,.05),transparent 40%)}
  .back-content{position:relative}
  .headline{font-size:21px;font-weight:700;font-style:italic;text-transform:uppercase;letter-spacing:.5px}
  .pitch{margin-top:14px;font-size:14px;text-transform:uppercase;line-height:1.5;letter-spacing:.2px}
  .back-rule{height:1px;background:rgba(255,255,255,.55);margin:26px 20px 14px}
  .back-tagline{font-size:13px;font-weight:700;text-transform:uppercase;letter-spacing:.3px}
</style>
</head>
<body>

<section class="card card-front" aria-label="Business card front">
  <div class="brand">
    <span class="brand-dot"></span>
    <span class="brand-name">Lantern Petro</span>
  </div>
  <p class="tagline">Lantern Petro, Powering the Nation's Oil &amp; Gas fields.</p>

  <div class="person">
    <h1 class="person-name"><span class="first">Dale</span> <span class="last">Winterholt</span></h1>
    <p class="person-role">Owner/CEO</p>
    <ul class="contact">
      <li><svg viewBox="0 0 24 24" aria-hidden="true"><path d="M6.6 10.8a15.1 15.1 0 0 0 6.6 6.6l2.2-2.2a1 1 0 0 1 1-.25 11.4 11.4 0 0 0 3.6.57 1 1 0 0 1 1 1V20a1 1 0 0 1-1 1A17 17 0 0 1 3 4a1 1 0 0 1 1-1h3.5a1 1 0 0 1 1 1c0 1.25.2 2.45.57 3.6a1 1 0 0 1-.25 1z"/></svg>701.555.0148</li>
      <li><svg viewBox="0 0 24 24" aria-hidden="true"><path d="M2 5h20v14H2zm2 2v.5l8 5 8-5V7l-8 5z"/></svg>Dwinterholt@lanternpetro.com</li>
      <li><svg viewBox="0 0 24 24" aria-hidden="true"><path d="M12 2a10 10 0 1 0 0 20 10 10 0 0 0 0-20zm6.9 9h-3a15 15 0 0 0-1.3-5.6A8 8 0 0 1 18.9 11zM12 4c.9 1.2 1.8 3.6 1.9 7h-3.8C10.2 7.6 11.1 5.2 12 4zM9.4 5.4A15 15 0 0 0 8.1 11h-3a8 8 0 0 1 4.3-5.6zM5.1 13h3a15 15 0 0 0 1.3 5.6A8 8 0 0 1 5.1 13zM12 20c-.9-1.2-1.8-3.6-1.9-7h3.8c-.1 3.4-1 5.8-1.9 7zm2.6-1.4a15 15 0 0 0 1.3-5.6h3a8 8 0 0 1-4.3 5.6z"/></svg>www.Lanternpetro.com</li>
    </ul>
  </div>

  <div class="divider"></div>
  <p class="locations"><span class="label">Locations:</span> Servicing the Powder River DJ Basin and Bakken Formations</p>
  <div class="base-band"></div>
</section>

<section class="card card-back" aria-label="Business card back">
  <div class="back-texture"></div>
  <div class="back-content">
    <h2 class="headline">Frac fueling is what we do.</h2>
    <p class="pitch">We understand how important diesel fuel is to your operation which is why our main service line is frac fueling. We assure our supply and stand by our service</p>
    <div class="back-rule"></div>
    <p class="back-tagline">Lantern Petro, Powering the Nation's Oil &amp; Gas fields.</p>
  </div>
</section>

</body>
</html>
```